Trifold brochure

Need a trifold marketing brochure for my autism therapy for children business . I would be interested in having designs in both English and Spanish if possible!!!!! Website is www.meadowlarkcareaba.com
Address on brochure needs to be 2718 Tamarind Ave W Suite 5
Minneapolis, MN 55192
Updates
Can you update the address on brochure to 2718 Tamarind Ave W Suite 5
Minneapolis, MN 55192
Target Market(s)
Autism therapy for children
Industry/Entity Type
Autism Therapy
Look and feel
Each slider illustrates characteristics of the customer's brand and the style your logo design should communicate.

```html
<!DOCTYPE html>
<html lang="en">
<head>
<meta charset="utf-8">
<title>Meadowlark Care Behavioral Therapy – Trifold Brochure</title>
<link rel="stylesheet" href="https://fonts.googleapis.com/css2?family=Montserrat:wght@400;500;600;700;800&family=Oswald:wght@500;600&family=Lora:ital,wght@1,500;1,600&display=swap">
<style>
:root{
  --blue:#1d5d98;
  --blue-deep:#174d82;
  --gold:#a97f3b;
  --gold-light:#c49a52;
  --ink:#232323;
  --white:#ffffff;
  --stage:#d6d6d6;
}
*{box-sizing:border-box;margin:0;padding:0}
html,body{width:1200px;height:3498px;overflow:hidden}
body{background:linear-gradient(#e4e4e4,var(--stage));font-family:"Montserrat",sans-serif;color:var(--ink);position:relative}
.spread{position:absolute;left:60px;width:1080px;height:830px;display:flex;box-shadow:0 18px 40px rgba(0,0,0,.25);background:var(--white)}
.spread--outside{top:780px}
.spread--inside{top:1890px}
.panel{position:relative;width:360px;height:830px;overflow:hidden}
.abs{position:absolute}
.photo{position:absolute;left:0;width:100%}
.brand{position:absolute;left:0;width:100%;text-align:center;font-family:"Montserrat",sans-serif;font-weight:600;line-height:1.15}
.brand__dot{display:block;width:34px;height:34px;border-radius:50%;margin:0 auto 10px}
.brand__name{display:block;font-size:22px;letter-spacing:.5px}
.brand__sub{display:block;font-size:13px;letter-spacing:1.2px}
.brand--blue{color:var(--blue)}.brand--blue .brand__dot{background:var(--blue)}
.brand--white{color:var(--white)}.brand--white .brand__dot{background:var(--white)}
.pill{position:absolute;left:50%;transform:translateX(-50%);border-radius:22px;display:flex;align-items:center;justify-content:center;gap:8px;font-weight:700;font-size:23px;letter-spacing:.5px;white-space:nowrap}
.pill svg{width:16px;height:16px}
.band{position:absolute;left:0;bottom:0;width:100%;height:50px;background:var(--gold);color:var(--white);display:flex;align-items:center;justify-content:center;font-size:15px;font-weight:500;letter-spacing:.6px}
/* about panel */
.about__title{position:absolute;left:30px;top:30px;color:var(--gold);font-weight:800;font-size:19px}
.about__text{position:absolute;left:30px;top:64px;width:300px;font-size:9.6px;line-height:1.5}
.pillar{position:absolute;left:28px;width:305px;display:flex;gap:10px}
.pillar__icon{flex:0 0 36px;height:36px;border-radius:50%;background:var(--gold);display:flex;align-items:center;justify-content:center}
.pillar__icon svg{width:20px;height:20px}
.pillar h3{color:var(--blue);font-size:16px;font-weight:700;margin-top:4px}
.pillar p{font-size:9.4px;line-height:1.5;margin-top:4px}
/* contact panel */
.contact{position:absolute;left:0;width:100%;text-align:center;color:var(--white)}
.contact__title{top:525px;font-size:14px;font-weight:600;letter-spacing:.6px}
.contact__icon{position:absolute;left:50%;transform:translateX(-50%);width:26px;height:26px;border-radius:50%;border:1.5px solid var(--gold-light);display:flex;align-items:center;justify-content:center}
.contact__icon svg{width:14px;height:14px}
.contact__line{font-size:10.5px;line-height:1.6}
/* hero panel */
.hero__head{position:absolute;left:0;top:520px;width:100%;text-align:center;font-family:"Oswald",sans-serif;font-weight:500;font-size:37px;line-height:1.1}
.hero__head .dark{color:var(--ink)}
.hero__head .gold{color:var(--gold)}
.tagline{font-family:"Lora",serif;font-style:italic;font-weight:500}
/* services */
.services__title{position:absolute;left:42px;top:30px;color:var(--blue);font-weight:800;font-size:26px;letter-spacing:.5px}
.services__rule{position:absolute;left:270px;top:48px;width:460px;height:2px;background:var(--blue)}
.card{position:absolute;width:226px;height:190px}
.card__photo{height:140px;width:100%}
.card__label{height:48px;display:flex;align-items:center;justify-content:center;text-align:center;color:var(--white);font-size:12px;font-weight:600;line-height:1.3;padding:0 10px}
.card__label--gold{background:var(--gold)}
.card__label--blue{background:var(--blue)}
.cta__head{position:absolute;left:0;top:185px;width:100%;text-align:center;font-family:"Oswald",sans-serif;font-weight:500;font-size:38px;line-height:1.15;color:var(--white)}
.cta__text{position:absolute;left:0;top:315px;width:100%;text-align:center;color:var(--white);font-size:17px;line-height:1.3}
.cta__web{position:absolute;left:0;top:445px;width:100%;text-align:center;color:var(--white);font-size:15px;font-weight:500}
.ring{position:absolute;left:50%;top:550px;transform:translateX(-50%);width:246px;height:246px;border-radius:50%;border:7px solid var(--gold);overflow:hidden}
</style>
</head>
<body>

<!-- OUTSIDE SPREAD -->
<section class="spread spread--outside">

  <!-- About panel -->
  <article class="panel panel--about">
    <h2 class="about__title">ABOUT ABA THERAPY</h2>
    <p class="about__text">ABA Therapy Applied Behavioral Analysis (ABA) Therapy is endorsed by national health and pediatric authorities and has been scientifically proven to be the most effective in helping a child with autism to acquire the necessary skills to reach their fullest potential. Research has proven that</p>

    <div class="pillar" style="top:160px">
      <div class="pillar__icon"><svg viewBox="0 0 20 20" fill="none" stroke="#fff" stroke-width="1.6"><circle cx="10" cy="10" r="7"/><circle cx="10" cy="10" r="3"/><path d="M10 1v4M10 15v4M1 10h4M15 10h4"/></svg></div>
      <div><h3>Vision</h3><p>To envision and strive towards a future where every child diagnosed with autism is supported, empowered, and equipped to achieve their fullest potential, fostering inclusivity and acceptance.</p></div>
    </div>
    <div class="pillar" style="top:268px">
      <div class="pillar__icon"><svg viewBox="0 0 20 20" fill="none" stroke="#fff" stroke-width="1.6"><circle cx="9" cy="11" r="7"/><circle cx="9" cy="11" r="3"/><path d="M9 11l9-9M14 2h4v4"/></svg></div>
      <div><h3>Mission</h3><p>We're dedicated to providing personalized, evidence-based therapy for every child with autism. Through early intervention and compassionate care, we empower growth and confidence, fostering thriving futures.</p></div>
    </div>
    <div class="pillar" style="top:388px">
      <div class="pillar__icon"><svg viewBox="0 0 20 20" fill="none" stroke="#fff" stroke-width="1.6"><path d="M2 17l6-11 4 6 2-3 4 8z"/><path d="M8 6V2l3 1.5L8 5"/></svg></div>
      <div><h3>Motto</h3><p>Unlocking Potential, Building Bridges, Illuminating Futures: Together, We Build Brighter Tomorrows.</p></div>
    </div>

    <div class="photo" style="top:520px;height:310px;background:linear-gradient(160deg,#efe9e2,#d9cfc4 55%,#b9aa98)" role="img" aria-label="Photo of a therapist playing with stacking toys alongside a young child on the floor"></div>
    <svg class="abs" style="left:0;top:500px" width="360" height="80" viewBox="0 0 360 80" preserveAspectRatio="none"><path d="M0 0H360V2Q120 -4 0 70Z" fill="#fff"/></svg>
  </article>

  <!-- Contact panel -->
  <article class="panel panel--contact">
    <div class="brand brand--blue" style="top:26px">
      <span class="brand__dot"></span>
      <span class="brand__name">MEADOWLARK CARE</span>
      <span class="brand__sub">BEHAVIORAL THERAPY</span>
    </div>
    <div class="photo" style="top:150px;height:340px;background:linear-gradient(120deg,#c9b7a6,#b5634e 45%,#2c3f73 75%,#e6ded5)" role="img" aria-label="Photo of a smiling boy building with colourful blocks"></div>
    <div class="photo" style="top:470px;height:360px;background:var(--blue)"></div>
    <svg class="abs" style="left:0;top:400px" width="360" height="80" viewBox="0 0 360 80" preserveAspectRatio="none">
      <path d="M0 80Q180 -10 360 80Z" fill="#1d5d98"/>
      <path d="M0 72Q180 -18 360 72" fill="none" stroke="#a97f3b" stroke-width="6"/>
    </svg>
    <div class="contact contact__title">CONTACT US</div>
    <div class="contact__icon" style="top:562px"><svg viewBox="0 0 14 14" fill="none" stroke="#c49a52" stroke-width="1.4"><path d="M7 13S2.5 8 2.5 5.2a4.5 4.5 0 0 1 9 0C11.5 8 7 13 7 13z"/><circle cx="7" cy="5.2" r="1.6"/></svg></div>
    <div class="contact contact__line" style="top:598px">2718 Tamarind Ave W Suite 5<br>Minneapolis, MN 55192</div>
    <div class="contact__icon" style="top:646px"><svg viewBox="0 0 14 14" fill="none" stroke="#c49a52" stroke-width="1.4"><rect x="1.5" y="3" width="11" height="8" rx="1"/><path d="M1.5 3.5L7 8l5.5-4.5"/></svg></div>
    <div class="contact contact__line" style="top:684px">info@meadowlarkcareaba.com</div>
    <div class="pill" style="top:724px;width:270px;height:40px;background:var(--white);color:var(--blue)">
      <svg viewBox="0 0 16 16" fill="#1d5d98"><path d="M3.5 1.5l2.5 3-1.5 1.5a8 8 0 0 0 5.5 5.5L11.5 10l3 2.5-1.5 2A11 11 0 0 1 1.5 3z"/></svg>612-555-0148</div>
    <div class="band">www.meadowlarkcareaba.com</div>
  </article>

  <!-- Cover panel -->
  <article class="panel panel--cover" style="background:var(--blue)">
    <div class="brand brand--white" style="top:26px">
      <span class="brand__dot"></span>
      <span class="brand__name">MEADOWLARK CARE</span>
      <span class="brand__sub">BEHAVIORAL THERAPY</span>
    </div>
    <div class="photo" style="top:150px;height:320px;background:linear-gradient(150deg,#2a6aa6,#8fa6c6 40%,#e0c9b5 60%,#5b87b8)" role="img" aria-label="Photo of a therapist helping a boy stack colourful rings at a table"></div>
    <div class="photo" style="top:460px;height:370px;background:var(--white)"></div>
    <svg class="abs" style="left:0;top:395px" width="360" height="80" viewBox="0 0 360 80" preserveAspectRatio="none">
      <path d="M0 80Q180 -10 360 80Z" fill="#fff"/>
      <path d="M40 60Q180 0 330 48" fill="none" stroke="#a97f3b" stroke-width="6"/>
    </svg>
    <h1 class="hero__head"><span class="dark">BUILDING BRIDGES TO</span><br><span class="gold">BRIGHTER FUTURES</span></h1>
    <p class="tagline abs" style="left:0;top:622px;width:100%;text-align:center;font-size:14px">Expert Autism Therapy Services</p>
    <div class="pill" style="top:724px;width:270px;height:40px;background:var(--blue);color:var(--white)">
      <svg viewBox="0 0 16 16" fill="#fff"><path d="M3.5 1.5l2.5 3-1.5 1.5a8 8 0 0 0 5.5 5.5L11.5 10l3 2.5-1.5 2A11 11 0 0 1 1.5 3z"/></svg>612-555-0148</div>
    <div class="band">www.meadowlarkcareaba.com</div>
  </article>
</section>

<!-- INSIDE SPREAD -->
<section class="spread spread--inside">
  <div class="panel" style="width:720px">
    <h2 class="services__title">OUR SERVICES</h2>
    <div class="services__rule"></div>

    <div class="card" style="left:42px;top:80px">
      <div class="card__photo" style="background:linear-gradient(120deg,#1f4f86,#3c6ea8 50%,#d9dde3)" role="img" aria-label="Photo of a boy in an ABA therapy session with a therapist"></div>
      <div class="card__label card__label--gold">Applied Behavior Analysis<br>(ABA) Therapy</div>
    </div>
    <div class="card" style="left:402px;top:80px">
      <div class="card__photo" style="background:linear-gradient(140deg,#e8e2d6,#d6c06a 55%,#3f73b3)" role="img" aria-label="Photo of a child doing hands-on occupational therapy play"></div>
      <div class="card__label card__label--blue">Occupational Therapy (OT)</div>
    </div>
    <div class="card" style="left:42px;top:300px">
      <div class="card__photo" style="background:linear-gradient(120deg,#f1efec,#d8d4cf 55%,#9fb4c8)" role="img" aria-label="Photo of a speech therapist working with a young girl"></div>
      <div class="card__label card__label--blue">Speech and Language Therapy</div>
    </div>
    <div class="card" style="left:402px;top:300px">
      <div class="card__photo" style="background:linear-gradient(120deg,#cfc6b8,#7f9aa6 50%,#b8a07f)" role="img" aria-label="Photo of children playing together at a table in a social skills group"></div>
      <div class="card__label card__label--gold">Social Skills Training</div>
    </div>

    <div class="photo" style="top:545px;height:285px;width:360px;background:linear-gradient(130deg,#d9cfc5,#d2503a 45%,#c8b39d)" role="img" aria-label="Photo of a mother and toddler playing with toy cars"></div>
    <div class="photo" style="left:360px;top:545px;height:285px;width:360px;background:linear-gradient(130deg,#2d5d8c,#c46a3a 40%,#6f8aa3 70%,#b08a4f)" role="img" aria-label="Photo of a child facing a large colourful puzzle wall"></div>
    <svg class="abs" style="left:0;top:520px" width="720" height="90" viewBox="0 0 720 90" preserveAspectRatio="none">
      <path d="M0 0H720V90Q540 -10 360 90Q180 -10 0 90Z" fill="#fff"/>
      <path d="M20 80Q180 -4 340 80" fill="none" stroke="#a97f3b" stroke-width="5"/>
      <path d="M380 80Q540 -4 700 80" fill="none" stroke="#a97f3b" stroke-width="5"/>
    </svg>
  </div>

  <article class="panel panel--cta" style="background:var(--blue)">
    <div class="brand brand--white" style="top:36px">
      <span class="brand__dot"></span>
      <span class="brand__name">MEADOWLARK CARE</span>
      <span class="brand__sub">BEHAVIORAL THERAPY</span>
    </div>
    <h2 class="cta__head">READY TO TAKE THE<br>NEXT STEP?</h2>
    <svg class="abs" style="left:172px;top:290px" width="16" height="16" viewBox="0 0 16 16"><path d="M8 0l2.2 5.3 5.8.5-4.4 3.8 1.3 5.7L8 12.3 3.1 15.3l1.3-5.7L0 5.8l5.8-.5z" fill="#c49a52"/></svg>
    <p class="cta__text tagline">Contact Us Today for Expert<br>Autism Therapy Services!</p>
    <div class="pill" style="top:385px;width:240px;height:38px;background:var(--gold);color:var(--white);font-size:22px">
      <svg viewBox="0 0 16 16" fill="#fff"><path d="M3.5 1.5l2.5 3-1.5 1.5a8 8 0 0 0 5.5 5.5L11.5 10l3 2.5-1.5 2A11 11 0 0 1 1.5 3z"/></svg>612-555-0148</div>
    <div class="cta__web">www.meadowlarkcareaba.com</div>
    <div class="ring"><div style="width:100%;height:100%;background:linear-gradient(120deg,#dfe3ea,#c7b9a6 50%,#7b99bd)" role="img" aria-label="Photo of a therapist and a young boy building with blocks"></div></div>
  </article>
</section>

</body>
</html>
```